Melissa Dorvan Personal Business Card

I like orange. It's would better if my card have an orange background
Address: 5820 Halvers Lane #417
San Jose
California
US
Tel: 4085172049

Industry/Entity Type

Business

```html
<!DOCTYPE html>
<html lang="en">
<head>
<meta charset="utf-8">
<title>Melissa Dorvan – Business Card</title>
<link href="https://fonts.googleapis.com/css2?family=Exo+2:wght@300;400;600&display=swap" rel="stylesheet">
<style>
  :root {
    --backdrop: #e8e5e1;
    --frost-top: #f4f4f4;
    --frost-bottom: #dcdcdc;
    --accent: #f27a1a;
    --accent-deep: #e0600b;
    --swoosh: #1d1d1d;
    --ink: #333333;
    --light-text: #ffffff;
  }
  * { box-sizing: border-box; margin: 0; padding: 0; }
  html, body {
    width: 1200px; height: 768px; overflow: hidden;
    background: var(--backdrop);
  }
  .canvas { position: relative; width: 1200px; height: 768px; }
  .card {
    position: absolute; left: 150px; top: 125px;
    width: 900px; height: 518px;
    background: linear-gradient(160deg, var(--frost-top), var(--frost-bottom));
    box-shadow: 0 14px 40px rgba(0,0,0,.18);
    overflow: hidden;
    font-family: "Exo 2", sans-serif;
  }
  .card-shapes { position: absolute; inset: 0; }
  .brand { position: absolute; left: 67px; top: 153px; width: 360px; height: 230px; }
  .brand-dot {
    position: absolute; left: 95px; top: 0;
    width: 144px; height: 144px; border-radius: 50%;
    background: var(--accent);
  }
  .brand-name {
    position: absolute; left: 0; top: 164px; white-space: nowrap;
    font-size: 46px; font-weight: 600; color: var(--ink);
    letter-spacing: .3px; line-height: 1;
  }
  .details { position: absolute; left: 601px; top: 0; color: var(--light-text); }
  .person-name { position: absolute; top: 82px; font-size: 25px; font-weight: 400; white-space: nowrap; line-height: 1; }
  .person-role { position: absolute; top: 114px; font-size: 18px; font-weight: 300; white-space: nowrap; line-height: 1; }
  .address { position: absolute; top: 224px; font-size: 17px; font-weight: 300; line-height: 25px; white-space: nowrap; }
  .contact-list { position: absolute; top: 343px; list-style: none; }
  .contact-list li {
    display: flex; align-items: center; gap: 10px;
    height: 25.5px; font-size: 15px; font-weight: 300; white-space: nowrap;
  }
  .contact-list svg { width: 15px; height: 15px; fill: var(--light-text); flex: none; }
</style>
</head>
<body>
<div class="canvas">
  <div class="card">
    <svg class="card-shapes" viewBox="0 0 900 518" preserveAspectRatio="none" aria-hidden="true">
      <defs>
        <linearGradient id="accentPanel" x1="0" y1="0" x2="1" y2="1">
          <stop offset="0" stop-color="var(--accent)"/>
          <stop offset="1" stop-color="var(--accent-deep)"/>
        </linearGradient>
      </defs>
      <path d="M455 0 C505 100 505 330 460 518 L900 518 L900 0 Z" fill="var(--swoosh)"/>
      <path d="M470 0 C520 95 528 300 492 518 L900 518 L900 0 Z" fill="url(#accentPanel)"/>
    </svg>

    <div class="brand">
      <div class="brand-dot"></div>
      <div class="brand-name">Melissa Dorvan</div>
    </div>

    <div class="details">
      <div class="person-name">Corin Ashby-Lane</div>
      <div class="person-role">consultant</div>
      <div class="address">5820 Halvers Lane #417<br>San Jose, CA</div>
      <ul class="contact-list">
        <li><svg viewBox="0 0 16 16"><path d="M3.5 1 L6 1 L7 4.5 L5.3 5.7 C6 7.5 8.5 10 10.3 10.7 L11.5 9 L15 10 L15 12.5 C15 14 13.8 15 12.5 15 C6.5 14.5 1.5 9.5 1 3.5 C1 2.2 2 1 3.5 1 Z"/></svg>408 517 2049</li>
        <li><svg viewBox="0 0 16 16"><path d="M4.5 0.5 h7 a1 1 0 0 1 1 1 v13 a1 1 0 0 1 -1 1 h-7 a1 1 0 0 1 -1 -1 v-13 a1 1 0 0 1 1 -1 Z M5 2.5 v9.5 h6 v-9.5 Z M8 12.8 a.8 .8 0 1 0 .01 0 Z"/></svg>408 517 2049</li>
        <li><svg viewBox="0 0 16 16"><path d="M4 1 h6 l2 2 v3 h-8 Z M2 7 h12 a1 1 0 0 1 1 1 v5 h-2 v2 h-10 v-2 h-2 v-5 a1 1 0 0 1 1 -1 Z M5 11 v3 h6 v-3 Z"/></svg>408 517 2049</li>
        <li><svg viewBox="0 0 16 16"><path d="M1 3 h14 v10 h-14 Z M2.2 4 L8 8.5 L13.8 4 Z"/></svg>hello@melissadorvan.com</li>
        <li><svg viewBox="0 0 16 16"><path d="M8 1 a7 7 0 1 0 .01 0 Z M8 2.3 c1 1.2 1.6 3 1.7 5 h-3.4 c.1-2 .7-3.8 1.7-5 Z M6.3 8.7 h3.4 c-.1 2-.7 3.8-1.7 5 c-1-1.2-1.6-3-1.7-5 Z M2.4 7.3 c.3-2.2 1.8-4 3.8-4.7 c-.8 1.3-1.2 2.9-1.3 4.7 Z M2.4 8.7 h2.5 c.1 1.8 .5 3.4 1.3 4.7 c-2-.7-3.5-2.5-3.8-4.7 Z M11.1 7.3 c-.1-1.8-.5-3.4-1.300-4.7 c2 .7 3.5 2.5 3.8 4.7 Z M11.1 8.7 h2.5 c-.3 2.2-1.8 4-3.8 4.7 c.8-1.3 1.2-2.9 1.3-4.7 Z"/></svg>www.melissadorvan.com</li>
      </ul>
    </div>
  </div>
</div>
</body>
</html>
```